New Plumbing Company

We are looking for a smart and creative business card design for our new plumbing company. We are looking for creativity and originality in our business cards.

Industry/Entity Type

Plumbing

Contact Information for Business Card

Crestline Plumbing
Peter Halvane
Managing Director
Telephone Number : 0481529604
Email : service@crestlineplumbing.com.au
Website : www.crestlineplumbing.com.au
Lic. 508264K

Colors
0692cd
33a6d7
000000

Requirements
Must have
• I want the business card to be designed on a black background using the blue tones i have selected as seen in the company logo.

```html
<!DOCTYPE html>
<html lang="en">
<head>
<meta charset="utf-8">
<title>Crestline Plumbing — Business Card Options</title>
<link rel="stylesheet" href="https://fonts.googleapis.com/css2?family=Questrial&family=Roboto:wght@300&display=swap">
<style>
  :root {
    --brand-blue: #177dc0;
    --brand-blue-light: #33a6d7;
    --icon-tint: #9cc4e6;
    --ink: #000000;
    --paper: #ffffff;
    --stage-top: #ffffff;
    --stage-bottom: #f2f2f4;
    --card-edge: #c9c9c9;
    --label-ink: #222222;
  }
  * { margin: 0; padding: 0; box-sizing: border-box; }
  html, body { width: 1200px; height: 800px; overflow: hidden; }
  body { font-family: "Questrial", sans-serif; position: relative; background: var(--stage-top); }

  .stage { position: absolute; left: 0; width: 1200px; height: 400px; }
  .stage--first { top: 0; background: var(--stage-top); }
  .stage--second { top: 400px; background: var(--stage-bottom); }

  .card { position: absolute; top: 85px; left: 399px; width: 402px; height: 230px; border: 1px solid var(--card-edge); overflow: hidden; background: var(--paper); }

  .band { position: absolute; left: 0; width: 100%; }
  .band--blue { background: var(--brand-blue); }
  .band--white { background: var(--paper); }
  .rule { position: absolute; left: 0; width: 100%; height: 4px; background: var(--ink); }

  .identity { position: absolute; }
  .identity__name { color: var(--brand-blue); font-size: 18px; line-height: 1; white-space: nowrap; }
  .identity__title { color: var(--ink); font-size: 10px; font-weight: bold; margin-top: 2px; margin-left: 5px; white-space: nowrap; letter-spacing: 0.2px; }

  .brand { position: absolute; display: flex; align-items: center; gap: 6px; }
  .brand__dot { width: 13px; height: 13px; border-radius: 50%; background: var(--brand-blue); }
  .brand__name { color: var(--brand-blue); font-size: 14px; white-space: nowrap; }

  .contacts { position: absolute; list-style: none; }
  .contacts li { display: flex; align-items: center; height: 21.5px; color: var(--paper); font-size: 14px; white-space: nowrap; }
  .contacts svg { width: 14px; height: 14px; margin-right: 8px; flex: none; }

  .option-label { position: absolute; left: 842px; top: 184px; font-family: "Roboto", sans-serif; font-weight: 300; font-size: 23px; letter-spacing: 1px; word-spacing: 4px; color: var(--label-ink); }
</style>
</head>
<body>

<svg width="0" height="0" style="position:absolute" aria-hidden="true">
  <defs>
    <symbol id="icon-phone" viewBox="0 0 14 14"><circle cx="7" cy="7" r="7" fill="var(--icon-tint)"/><path d="M4.5 3.5l1.5 0 .6 2-1 .8a5 5 0 0 0 2.3 2.3l.8-1 2 .6v1.5c0 .5-.4.8-.9.8A6.2 6.2 0 0 1 3.7 4.4c0-.5.3-.9.8-.9z" fill="var(--brand-blue)"/></symbol>
    <symbol id="icon-mail" viewBox="0 0 14 14"><rect x="0.5" y="3" width="13" height="9" fill="var(--icon-tint)"/><path d="M0.5 3l6.5 5 6.5-5M0.5 12l4.8-4.5M13.5 12l-4.8-4.5" stroke="var(--brand-blue)" stroke-width="1" fill="none"/></symbol>
    <symbol id="icon-web" viewBox="0 0 14 14"><circle cx="7" cy="7" r="6.5" fill="var(--icon-tint)"/><path d="M0.5 7h13M7 0.5c-2.5 3-2.5 10 0 13M7 0.5c2.5 3 2.5 10 0 13M2 3.5h10M2 10.5h10" stroke="var(--brand-blue)" stroke-width="0.9" fill="none"/></symbol>
    <symbol id="icon-licence" viewBox="0 0 14 14"><rect x="1.5" y="0.5" width="11" height="10" rx="1" fill="none" stroke="var(--icon-tint)" stroke-width="1.4"/><path d="M4 3.5h6M4 6h4" stroke="var(--icon-tint)" stroke-width="1.2"/><path d="M4 9v5l1.5-1.2L7 14V9" fill="var(--icon-tint)"/></symbol>
  </defs>
</svg>

<section class="stage stage--first">
  <article class="card">
    <div class="band band--white" style="top:0;height:89px"></div>
    <div class="rule" style="top:89px"></div>
    <div class="band band--blue" style="top:93px;height:137px"></div>

    <div class="identity" style="left:60px;top:31px">
      <p class="identity__name">Peter Halvane</p>
      <p class="identity__title">Managing Director</p>
    </div>
    <div class="brand" style="left:222px;top:36px">
      <span class="brand__dot"></span><span class="brand__name">Crestline Plumbing</span>
    </div>

    <ul class="contacts" style="left:38px;top:117px">
      <li><svg><use href="#icon-phone"/></svg>0481529604</li>
      <li><svg><use href="#icon-mail"/></svg>service@crestlineplumbing.com.au</li>
      <li><svg><use href="#icon-web"/></svg>www.crestlineplumbing.com.au</li>
      <li><svg><use href="#icon-licence"/></svg>508264K</li>
    </ul>
  </article>
  <p class="option-label">OPTION 01</p>
</section>

<section class="stage stage--second">
  <article class="card">
    <div class="band band--blue" style="top:0;height:72px"></div>
    <div class="rule" style="top:72px"></div>
    <div class="band band--white" style="top:76px;height:77px"></div>
    <div class="rule" style="top:153px"></div>
    <div class="band band--blue" style="top:157px;height:73px"></div>

    <ul class="contacts" style="left:33px;top:20px">
      <li><svg><use href="#icon-phone"/></svg>0481529604</li>
      <li><svg><use href="#icon-mail"/></svg>service@crestlineplumbing.com.au</li>
    </ul>

    <div class="identity" style="left:48px;top:98px">
      <p class="identity__name">Peter Halvane</p>
      <p class="identity__title">Managing Director</p>
    </div>
    <div class="brand" style="left:228px;top:105px">
      <span class="brand__dot"></span><span class="brand__name">Crestline Plumbing</span>
    </div>

    <ul class="contacts" style="left:33px;top:163px">
      <li><svg><use href="#icon-web"/></svg>www.crestlineplumbing.com.au</li>
      <li><svg><use href="#icon-licence"/></svg>508264K</li>
    </ul>
  </article>
  <p class="option-label">OPTION 02</p>
</section>

</body>
</html>
```